Hot young IT advisor needs business cards as upscale and innovative as they are

We need business cards that make a statement about who we are, as a young and upscale IT advisor. Our whole angle is innovation and tenacity in our personal relationships with our clients. We've just done a brand overhaul and need cards that have the new logos, but we're also looking for someone with a sixth sense who can capture what sets us apart and communicate that with a business card. Clean, minimalist, upscale, innovative, personal. Our budget only allows room for them to be soft-touch, no spot gloss or foil designs please.

Target Market(s)

High-level decision makers at middle-market and large organizations in the healthcare, financial services, sports and entertainment, K-12 education, college and university, state and local government, and federal government sectors.

Industry/Entity Type

Information Technology

Font styles to use
Sans Serif

Colors
ec1f27
606060
ffffff

Requirements
Should not have
• Designs with low contrast which would require spot-gloss or embossing.

```html
<!DOCTYPE html>
<html lang="en">
<head>
<meta charset="utf-8">
<title>LUMENVALE Business Card</title>
<link href="https://fonts.googleapis.com/css2?family=Montserrat:wght@400;600;700&family=Open+Sans:wght@400&display=swap" rel="stylesheet">
<style>
  :root {
    --brand-red: #ec1f27;
    --brand-grey: #606060;
    --ink: #2b2b2b;
    --paper: #ffffff;
    --card-black: #0e0e0e;
    --card-black-soft: #2a2a2a;
    --backdrop: #e9e7e4;
  }
  * { margin: 0; padding: 0; box-sizing: border-box; }
  html, body { width: 1200px; height: 900px; overflow: hidden; }
  body {
    background: var(--backdrop);
    position: relative;
    font-family: "Open Sans", Arial, sans-serif;
  }
  .card {
    position: absolute;
    left: 285px;
    width: 630px;
    height: 360px;
    border-radius: 4px;
    box-shadow: 0 10px 30px rgba(0,0,0,0.18);
    overflow: hidden;
  }
  /* Back side */
  .card-back {
    top: 50px;
    background: linear-gradient(135deg, var(--card-black) 0%, var(--card-black) 45%, var(--card-black-soft) 100%);
    display: flex;
    align-items: center;
    justify-content: center;
    gap: 16px;
  }
  .card-back .mark-square {
    width: 22px; height: 22px;
    background: var(--brand-red);
  }
  .card-back .brand-name {
    font-family: "Montserrat", Arial, sans-serif;
    font-weight: 600;
    font-size: 34px;
    letter-spacing: 6px;
    color: var(--brand-red);
  }
  /* Front side */
  .card-front {
    top: 470px;
    background: linear-gradient(160deg, var(--paper) 0%, var(--paper) 55%, #f1f0f0 100%);
  }
  .holder {
    position: absolute;
    left: 48px;
    top: 40px;
  }
  .holder-name {
    font-family: "Montserrat", Arial, sans-serif;
    font-weight: 700;
    font-size: 25px;
    letter-spacing: -0.5px;
    color: var(--ink);
    line-height: 1.1;
  }
  .holder-title {
    font-family: "Montserrat", Arial, sans-serif;
    font-weight: 400;
    font-size: 17px;
    letter-spacing: 1px;
    color: var(--brand-red);
    margin-top: 2px;
  }
  .holder-rule {
    width: 44px;
    height: 3px;
    background: var(--brand-red);
    margin-top: 20px;
  }
  .wordmark {
    position: absolute;
    right: 40px;
    top: 66px;
    font-family: "Montserrat", Arial, sans-serif;
    font-weight: 400;
    font-size: 34px;
    letter-spacing: 5px;
    color: var(--brand-grey);
  }
  .contact-list {
    position: absolute;
    left: 48px;
    bottom: 38px;
    list-style: none;
  }
  .contact-item {
    display: flex;
    align-items: center;
    gap: 12px;
    font-size: 19px;
    color: var(--ink);
    line-height: 1;
    margin-top: 12px;
  }
  .contact-icon { width: 18px; height: 18px; flex: none; }
  .contact-icon * { stroke: var(--brand-red); fill: none; stroke-width: 1.6; }
  .contact-icon .solid { fill: var(--brand-red); stroke: none; }
</style>
</head>
<body>
  <section class="card card-back" aria-label="Card back">
    <span class="mark-square"></span>
    <span class="brand-name">LUMENVALE</span>
  </section>

  <section class="card card-front" aria-label="Card front">
    <div class="holder">
      <p class="holder-name">YOUR NAME</p>
      <p class="holder-title">JOB TITLE</p>
      <div class="holder-rule"></div>
    </div>

    <p class="wordmark">LUMENVALE</p>

    <ul class="contact-list">
      <li class="contact-item">
        <svg class="contact-icon" viewBox="0 0 18 18" aria-hidden="true">
          <rect x="5" y="1.5" width="8" height="15" rx="1.5"/>
          <line x1="8" y1="13.5" x2="10" y2="13.5"/>
        </svg>
        <span>000 000 0000</span>
      </li>
      <li class="contact-item">
        <svg class="contact-icon" viewBox="0 0 18 18" aria-hidden="true">
          <rect class="solid" x="1.5" y="4" width="15" height="10" rx="1"/>
          <polyline points="1.5,4.5 9,10 16.5,4.5" style="stroke:#fff"/>
        </svg>
        <span>youremail@xyz.com</span>
      </li>
      <li class="contact-item">
        <svg class="contact-icon" viewBox="0 0 18 18" aria-hidden="true">
          <circle cx="9" cy="9" r="7.5"/>
          <ellipse cx="9" cy="9" rx="3.2" ry="7.5"/>
          <line x1="1.5" y1="9" x2="16.5" y2="9"/>
          <line x1="3" y1="5" x2="15" y2="5"/>
          <line x1="3" y1="13" x2="15" y2="13"/>
        </svg>
        <span>www.yourwebsite.com</span>
      </li>
    </ul>
  </section>
</body>
</html>
```